Hardcore nerd needs to stand out in a sea of dull Defence business cards

Wombat Devices is a new Australian consulting engineering company that turns research and theory into practical systems. No evangelistic fluff, just mathematics and physics into electronic and optical circuits for consumer products, scientific research or Defence applications.

We already have a recognised logo (provided) which is often dark blue/black on a light background but we're open to other combinations. (Us engineers tend to have limited aesthetic imagination :)

Some of our recent products have included:
* Instrumentation for electrical testing,
* Radar jammers,
* GPS antenna design,
* Satellite tracking systems,
* High power lasers

We're open to both single and double-sided designs - happy to be convinced either way.

P.S. Another group is working on the web page, so - alas - our web site is currently of no use for images/ideas...

Target Market(s)

Engineering managers,
Scientists

Contact Information for Business Card

Dr Colin Marsh
R&D Engineer

colin@wombatdevicesco.com.au
0427 563 210

PO Box XXX (to be confirmed)
Banks ACT 2913
Australia

Font styles to use
Serif
Sans Serif

Colors

Designer to choose colors to be used in the design.

Requirements
Must have
• My contact details!
• I've had many (great) "bold and plain" designs submitted already, so feel free to be artistically creative :)
• Happy to take advice re fonts/colours/printability etc.
Nice to have
• I'm not sure if "lists" are more at home on a CV than a business card, but representative services include:
• Applied electromagnetics
• RF and high speed electronics
• Signal and image processing
• Electro-optical and laser systems
• Concept-to-prototype design services
• If you're considering double sided cards, then often measuring/alignment grids/rulers feature on the back of similar cards.
• e.g. https://www.lumoptix-example.com/newgrouppage9.cfm?objectgroup_id=4815
• https://www.lumoptix-example.com/newgrouppage9.cfm?objectgroup_ID=4817
• ..or even a "Smith chart" (google will return lots)
• Generic images to represent a capability might work - googling images associated with keyword for each of these areas might help:
• - "passive radar", "phased array", "fdtd", "vircator"
• RF and high speed electronic design
• - "smith chart", "microstrip circuits", "dimensioned drawing", "electronic schematic"
• - "dft", "iir filter"
• - "optical cavity". "laser energy level diagram"
• Background/watermarked images outlines/wireframes/schematics would probably look OK.
Should not have
• If a list of projects/services is provided, it is important not to make the client feel that this is "all" the company can do. Engineering design is a creative discipline (like graphics :)
• Please, no stock "military" snaps like planes, missiles, etc!

```html
<!DOCTYPE html>
<html lang="en">
<head>
<meta charset="utf-8">
<title>Wombat Devices – Business Card</title>
<link href="https://fonts.googleapis.com/css2?family=Roboto:wght@400;500;700&display=swap" rel="stylesheet">
<style>
  :root {
    --navy: #012f72;
    --navy-deep: #021f5e;
    --ink: #444444;
    --paper: #ffffff;
    --backdrop: #e4e4e4;
  }
  html, body {
    margin: 0;
    width: 1200px;
    height: 1200px;
    overflow: hidden;
    background: var(--backdrop);
    font-family: "Roboto", Arial, sans-serif;
  }
  .card {
    position: absolute;
    left: 200px;
    width: 800px;
    height: 457px;
    border-radius: 26px;
    overflow: hidden;
  }
  .card-front { top: 100px; background: var(--paper); }
  .card-back {
    top: 640px;
    background: linear-gradient(180deg, var(--navy) 0%, var(--navy-deep) 100%);
    color: var(--paper);
  }

  /* Front */
  .name-band {
    position: absolute;
    left: 0; top: 43px;
    width: 480px; height: 105px;
    background: var(--navy);
    color: var(--paper);
  }
  .person-name {
    position: absolute;
    left: 47px; top: 28px;
    margin: 0;
    font-size: 27px;
    font-weight: 700;
  }
  .person-role {
    position: absolute;
    left: 47px; top: 62px;
    margin: 0;
    font-size: 19px;
    font-weight: 400;
  }
  .brand-dot {
    position: absolute;
    left: 455px; top: 43px;
    width: 106px; height: 106px;
    border-radius: 50%;
    background: var(--navy);
  }
  .brand-name {
    position: absolute;
    left: 572px; top: 66px;
    margin: 0;
    color: var(--navy);
    font-size: 31px;
    font-weight: 700;
    line-height: 32px;
    letter-spacing: 1px;
    text-transform: uppercase;
  }
  .contact-list {
    position: absolute;
    left: 47px; top: 350px;
    margin: 0; padding: 0;
    list-style: none;
    color: var(--ink);
    font-size: 18px;
    line-height: 23px;
  }
  .contact-list li { display: flex; align-items: center; gap: 9px; }
  .contact-list svg { width: 15px; height: 15px; fill: var(--navy); flex: none; }
  .postal-address {
    position: absolute;
    right: 44px; top: 351px;
    margin: 0;
    text-align: right;
    font-style: normal;
    color: var(--ink);
    font-size: 18px;
    line-height: 23px;
  }

  /* Back */
  .back-emblem {
    position: absolute;
    left: 319px; top: 70px;
    width: 162px; height: 162px;
    border-radius: 50%;
    background: var(--paper);
  }
  .back-brand {
    position: absolute;
    left: 0; right: 0; top: 262px;
    margin: 0;
    text-align: center;
    font-size: 30px;
    font-weight: 700;
    letter-spacing: 3px;
    text-transform: uppercase;
  }
  .services {
    position: absolute;
    left: 0; right: 0; top: 357px;
    margin: 0;
    text-align: center;
    font-size: 18.5px;
    line-height: 22.5px;
  }
</style>
</head>
<body>

<section class="card card-front" aria-label="Business card front">
  <div class="name-band">
    <h1 class="person-name">Dr Colin Marsh</h1>
    <p class="person-role">R&amp;D Engineer</p>
  </div>
  <div class="brand-dot" aria-hidden="true"></div>
  <p class="brand-name">Wombat<br>Devices</p>

  <ul class="contact-list">
    <li>
      <svg viewBox="0 0 24 24" aria-hidden="true"><path d="M6.6 10.8a15.1 15.1 0 0 0 6.6 6.6l2.2-2.2a1 1 0 0 1 1-.25 11.4 11.4 0 0 0 3.6.57 1 1 0 0 1 1 1V20a1 1 0 0 1-1 1A17 17 0 0 1 3 4a1 1 0 0 1 1-1h3.5a1 1 0 0 1 1 1c0 1.25.2 2.45.57 3.57a1 1 0 0 1-.25 1z"/></svg>
      0427 563 210
    </li>
    <li>
      <svg viewBox="0 0 24 24" aria-hidden="true"><path d="M2 5h20v14H2z M3.5 6.5 12 13l8.5-6.5" fill="var(--navy)" stroke="#fff" stroke-width="1.6"/></svg>
      colin@wombatdevicesco.com.au
    </li>
    <li>
      <svg viewBox="0 0 24 24" aria-hidden="true"><circle cx="12" cy="12" r="10"/><path d="M8 6c2 1 3 3 1.5 4.5S7 13 9 15s1 4 1 4M15 5c-1 2 1 3 2.5 4s1 3-.5 4-1 3 0 4" stroke="#fff" stroke-width="1.6" fill="none"/></svg>
      www.wombatdevicesco.com.au
    </li>
  </ul>

  <address class="postal-address">
    PO Box 318<br>
    Banks ACT 2913<br>
    Australia
  </address>
</section>

<section class="card card-back" aria-label="Business card back">
  <div class="back-emblem" aria-hidden="true"></div>
  <p class="back-brand">Wombat Devices</p>
  <p class="services">
    Applied electromagnetics&thinsp;•&thinsp;RF &amp; high speed electronics<br>
    Signal &amp; image processing&thinsp;•&thinsp;Electro-optical &amp; laser systems<br>
    Concept-to-prototype design services
  </p>
</section>

</body>
</html>
```